Retail Jewelry Business Card Design Project

We are in need of a new business card design for a retail jewelry store. This store is in the business of fine jewelry including but not specific to bridal jewelry, diamonds, designer jewelry and watches.

This store has been in business for 20 years but continues to strive for a modern professional appeal. The main colors use for this business are a royal blue, white and silver.

Target Market(s)

Target market is ages 18-50

Industry/Entity Type

Jewelry

Requirements
Must have
• Sales Person Name
Sales Person Email Address

Store Address
Store Phone
Website

Standard business card size. No odd shapes or sizes.
Nice to have
• Overall modern feel for card.

We have thought that a design with a nice feature of the logo on the back of the card would be nice but open to ideas.
Should not have
• No specific images of jewelry should be used.

```html
<!DOCTYPE html>
<html lang="en">
<head>
<meta charset="utf-8">
<title>Marlowe Hart Fine Jewelry – Business Card</title>
<link rel="stylesheet" href="https://fonts.googleapis.com/css2?family=Cinzel:wght@400&family=Questrial&display=swap">
<style>
  :root {
    --backdrop: #c2bfb3;
    --royal-blue: #1a1f8c;
    --link-blue: #2b2f9e;
    --ink: #333338;
    --paper: #ffffff;
    --silver-light: #f7f8fa;
    --silver-mid: #e4e6ea;
    --silver-dark: #d2d5db;
  }
  * { margin: 0; padding: 0; box-sizing: border-box; }
  html, body {
    width: 1200px; height: 900px; overflow: hidden;
    background: var(--backdrop);
  }
  .canvas { position: relative; width: 1200px; height: 900px; }

  .card {
    position: absolute;
    width: 656px; height: 378px;
    background:
      linear-gradient(115deg, var(--silver-mid) 0%, var(--silver-light) 22%, var(--silver-dark) 38%, var(--silver-light) 55%, var(--silver-mid) 72%, var(--silver-light) 88%, var(--silver-mid) 100%);
    border: 1px solid #b9bbbf;
  }
  .card-face {
    position: absolute;
    background: var(--paper);
  }
  .card--back { left: 475px; top: 58px; }
  .card--back .card-face { left: 28px; top: 28px; width: 599px; height: 324px; border: 1px solid var(--silver-dark); }
  .card--front { left: 63px; top: 460px; }
  .card--front .card-face { left: 29px; top: 27px; width: 600px; height: 323px; }

  .store-mark {
    position: absolute; left: 0; right: 0; top: 136px;
    display: flex; align-items: center; justify-content: center; gap: 14px;
  }
  .store-mark-square {
    width: 14px; height: 14px;
    background: var(--royal-blue);
  }
  .store-mark-name {
    font-family: "Questrial", sans-serif; font-weight: 400;
    font-size: 30px; line-height: 1;
    color: var(--royal-blue);
  }

  .person-name {
    position: absolute; left: 0; right: 0; top: 98px;
    text-align: center;
    font-family: "Cinzel", serif; font-weight: 400;
    font-size: 23px; letter-spacing: 0.08em;
    color: var(--royal-blue);
  }
  .person-email {
    position: absolute; left: 0; right: 0; top: 137px;
    text-align: center;
    font-family: "Questrial", sans-serif;
    font-size: 16px; letter-spacing: 0.09em;
    color: var(--ink);
  }
  .store-address {
    position: absolute; left: 32px; top: 250px;
    font-family: "Questrial", sans-serif; font-style: normal;
    font-size: 16px; line-height: 28px;
    color: var(--ink);
  }
  .store-website {
    position: absolute; right: 41px; top: 273px;
    font-family: "Questrial", sans-serif;
    font-size: 17px; letter-spacing: 0.02em;
    color: var(--link-blue);
  }
</style>
</head>
<body>
<main class="canvas">
  <section class="card card--back" aria-label="Card back">
    <div class="card-face">
      <div class="store-mark">
        <span class="store-mark-square" aria-hidden="true"></span>
        <h1 class="store-mark-name">Marlowe Hart Fine Jewelry</h1>
      </div>
    </div>
  </section>

  <section class="card card--front" aria-label="Card front">
    <div class="card-face">
      <h2 class="person-name">Marlowe Hart Avenell</h2>
      <p class="person-email">marlowe@marlowehartjewelry.com</p>
      <address class="store-address">2280 Linden Avenue<br>Harbor Point, FL 32990</address>
      <p class="store-website">www.marlowehartjewelry.com</p>
    </div>
  </section>
</main>
</body>
</html>
```